Harlow Ridge Beard Oil Label for 1oz dropper bottle

Create a label for a 1oz beard oil dropper bottle. The label is 1.5 inches tall and 2.75 inches wide. Our logo is listed in the brief so please use it but it doesnt have to be that prominent. BEARD OIL is the most important verbiage. We like elements of all the attached images but we want our own look and feel.

Target Market(s)

Men with beards

Requirements
Must have
• Harlow Ridge Logo, BEARD OIL, Flavor (Tobacco Vanilla)

Ingredients
Fractionated Coconut Oil (MCT)
Golden Jojoba Oil
Hemp Seed Oil
Tea Tree Essential Oil
Orange Bitter Essential Oil
Peppermint Supreme Essential Oil
Vireo Aromas
DYE FREE

Directions:
Directions: apply 3-6 drops into your hand...rub oil into hands and apply directly onto beard. For best results massage into skin under beard area and work oil out towards beard. Discontinue use if skin becomes irritated.

100% MADE IN THE USA (American Flag 1 color)
Veteran Owned Co.
Nice to have
• Labels can change color with each flavor or a ring can change color to show flavor.

```html
<!DOCTYPE html>
<html lang="en">
<head>
<meta charset="utf-8">
<title>Harlow Ridge Beard Oil Label</title>
<link href="https://fonts.googleapis.com/css2?family=Andika:wght@400;700&family=Abril+Fatface&family=Yellowtail&family=Old+Standard+TT&display=swap" rel="stylesheet">
<style>
  :root {
    --ink: #111111;
    --paper: #ffffff;
    --label-bg: #f5f5f5;
    --rule: #4a2a1f;
    --beard-light: #b9b9b9;
    --beard-dark: #3d3d3d;
    --flag-stripe: #111111;
  }
  * { margin: 0; padding: 0; box-sizing: border-box; }
  html, body {
    width: 1200px; height: 525px; overflow: hidden;
    background: var(--paper);
  }
  .canvas { position: relative; width: 1200px; height: 525px; }
  .label {
    position: absolute; left: 119px; top: 0;
    width: 962px; height: 525px;
    background: var(--label-bg);
    color: var(--ink);
    font-family: "Andika", sans-serif;
    overflow: hidden;
  }
  .abs { position: absolute; }
  .side-info {
    left: 0; width: 252px; text-align: center;
    font-size: 14px; line-height: 21.6px;
  }
  .rule { position: absolute; height: 2px; background: var(--rule); }
  .flag { left: 65px; top: 360px; width: 124px; height: 65px; }
  .tagline {
    left: 218px; top: 27px; height: 470px;
    writing-mode: vertical-rl;
    font-family: "Old Standard TT", serif;
    font-size: 22px; letter-spacing: 4px;
    text-align: center;
  }
  .beard-art {
    left: 447px; top: 4px; width: 92px; height: 105px;
    background: radial-gradient(ellipse at 50% 40%, var(--beard-light), var(--beard-dark));
    border-radius: 40% 40% 50% 50%;
  }
  .brand {
    left: 280px; top: 128px; width: 403px; text-align: center;
    font-family: "Andika", sans-serif; font-weight: 700;
    font-size: 66px; line-height: 74px; letter-spacing: 2px;
  }
  .product {
    left: 280px; top: 286px; width: 403px; text-align: center;
    font-family: "Abril Fatface", serif;
    font-size: 60px; line-height: 66px; letter-spacing: 1px;
    border-bottom: 3px solid var(--ink);
  }
  .brush {
    left: 325px; top: 400px; width: 390px; height: 78px;
    background: var(--ink);
    transform: rotate(-20deg);
  }
  .flavor {
    left: 360px; top: 392px; width: 330px; text-align: center;
    font-family: "Yellowtail", cursive;
    color: var(--paper); font-size: 44px; line-height: 46px;
    transform: rotate(-20deg);
  }
  .volume { left: 583px; top: 480px; font-size: 14px; }
  .details {
    left: 722px; width: 196px; text-align: center;
    font-size: 14px; line-height: 21.6px; letter-spacing: 0.3px;
  }
  .details h2 { font-size: 19px; font-weight: 700; line-height: 24px; }
</style>
</head>
<body>
<div class="canvas">
  <div class="label">
    <p class="abs side-info" style="top:48px;">Original BEARD OIL<br>Posses a<br>MASCULINE SCENT<br>and a light<br>Character as it<br>gently Moisturizes<br>Your face.</p>
    <div class="rule" style="left:35px; top:215px; width:163px;"></div>
    <p class="abs side-info" style="top:233px;">Use 2 - 3 times<br>per week</p>
    <div class="rule" style="left:35px; top:290px; width:163px;"></div>
    <p class="abs side-info" style="top:309px;">Original<br>100 % made in USA</p>
    <svg class="abs flag" viewBox="0 0 124 65" aria-label="One colour American flag">
      <g fill="var(--flag-stripe)">
        <rect x="0" y="0" width="124" height="5"/>
        <rect x="0" y="10" width="124" height="5"/>
        <rect x="0" y="20" width="124" height="5"/>
        <rect x="0" y="30" width="124" height="5"/>
        <rect x="0" y="40" width="124" height="5"/>
        <rect x="0" y="50" width="124" height="5"/>
        <rect x="0" y="60" width="124" height="5"/>
        <rect x="0" y="0" width="52" height="35"/>
      </g>
    </svg>
    <p class="abs side-info" style="top:446px;">Veteran Owned Co.</p>

    <p class="abs tagline">QUALITY &amp; CRAFTSMANSHIP</p>

    <div class="abs beard-art" role="img" aria-label="Grey illustrated beard"></div>
    <p class="abs brand">HARLOW<br>RIDGE</p>
    <h1 class="abs product">BEARD OIL</h1>
    <div class="abs brush" role="img" aria-label="Black brush stroke behind the flavour name"></div>
    <p class="abs flavor">Tobacco<br>Vanilla</p>
    <p class="abs volume">30 ML / 1FL.OZ</p>

    <div class="abs details" style="top:20px;">
      <h2>Ingredients</h2>
      <p>Fractionated Coconut Oil<br>(MCT), Golden Jojoba Oil,<br>Hemp Seed Oil,<br>Tea Tree Essential Oil,<br>Orange Bitter Essential<br>Oil, Peppermint Supreme<br>Essential Oil, Vireo Aromas<br>DYE FREE</p>
    </div>
    <div class="rule" style="left:747px; top:233px; width:163px;"></div>
    <div class="abs details" style="top:247px;">
      <h2>Directions:</h2>
      <p>Apply 3-6 drops into your<br>hand...rub oil into hands<br>and apply directly onto<br>beard. For best results<br>massage into skin under<br>beard area and work oil<br>out towards beard.</p>
    </div>
    <div class="rule" style="left:747px; top:434px; width:163px;"></div>
    <p class="abs details" style="top:446px;">***Discontinue use if<br>skin becomes irritated.</p>
  </div>
</div>
</body>
</html>
```